Business Card Design Project

We need a simple business card design that uses our current logo.
We need to have the current logo put into a high res format.
We need to have 1 card made with contact information.
We will supply the information for the 4 employees.
Industry/Entity Type
Business
Requirements
Must have
- The contact information is as follows:
Paul Vardenko
Producer/CEO
c. 949-555-0148
f. 650-555-0193
paulv@lanternyardstudio.example
Mel Trosgaard, CFO
c. 949-555-0172
f. 650-555-0193
melt@lanternyardstudio.example
Paul Brenneky, PR
c. 267-555-0126
f. 650-555-0193
pbrenneky@lanternyardstudio.example
Dale Furnow, Producer
c. 949-555-0164
f. 650-555-0193
dalef@lanternyardstudio.example
The address for all cards is:
318 W Calle Norvista #2715, San Clemente, CA 92631

```html
<!DOCTYPE html>
<html lang="en">
<head>
<meta charset="utf-8">
<title>Lantern Yard Studio – Business Card</title>
<link rel="stylesheet" href="https://fonts.googleapis.com/css2?family=Cinzel:wght@400&family=Questrial&display=swap">
<style>
  :root {
    --paper: #ffffff;
    --brand-blue: #0a55d6;
    --name-blue: #1a4fd0;
    --ink: #111111;
  }
  * { margin: 0; padding: 0; box-sizing: border-box; }
  html, body {
    width: 1200px;
    height: 734px;
    overflow: hidden;
    background: var(--paper);
  }
  .card {
    position: relative;
    width: 1200px;
    height: 734px;
    background: var(--paper);
  }
  .wordmark {
    position: absolute;
    left: 124px;
    top: 128px;
    width: 870px;
    font-family: "Questrial", sans-serif;
    font-size: 70px;
    line-height: 1;
    letter-spacing: 1px;
    color: var(--ink);
    white-space: nowrap;
  }
  .divider {
    position: absolute;
    left: 0;
    top: 282px;
    width: 1200px;
    height: 19px;
    background: var(--brand-blue);
  }
  .person {
    position: absolute;
    left: 700px;
    top: 372px;
    width: 476px;
    text-align: center;
    font-family: "Cinzel", serif;
    color: var(--name-blue);
  }
  .person-name {
    font-size: 46px;
    line-height: 54px;
    font-weight: 400;
    white-space: nowrap;
  }
  .person-title {
    font-size: 40px;
    line-height: 52px;
  }
  .contact {
    position: absolute;
    right: 76px;
    top: 512px;
    text-align: right;
    font-family: "Questrial", sans-serif;
    font-size: 38px;
    line-height: 52px;
    color: var(--ink);
    list-style: none;
  }
</style>
</head>
<body>
  <main class="card">
    <div class="wordmark">LANTERN YARD STUDIO</div>
    <div class="divider"></div>
    <div class="person">
      <h1 class="person-name">Mel Trosgaard</h1>
      <p class="person-title">CFO</p>
    </div>
    <ul class="contact">
      <li class="contact-cell">Cell: 949-555-0172</li>
      <li class="contact-fax">Fax: 650-555-0193</li>
      <li class="contact-email">melt@lanternyardstudio.example</li>
    </ul>
  </main>
</body>
</html>
```